Harvest of Kingdoms
preparing the way of the Lord...
Modern
Tom Farrel
412 Co.Rd. 118 Marlow, Pa.17602
tomjane4Faith@postvale.com
www.tf-harvestofkingdoms.com
preaching the gospel of Jesus, and teaching others to do the same.
mission trips
rallies and revivals
camps
this is for business cards and letterhead...

```html
<!DOCTYPE html>
<html lang="en">
<head>
<meta charset="utf-8">
<title>Harvest of Kingdoms – Business Card</title>
<link rel="stylesheet" href="https://fonts.googleapis.com/css2?family=Source+Sans+3:wght@400&display=swap">
<style>
  :root {
    --card: #ffffff;
    --ink: #111111;
    --band: #000000;
    --accent: #2e8b3a;
  }
  * { margin: 0; padding: 0; box-sizing: border-box; }
  html, body {
    width: 1200px;
    height: 751px;
    overflow: hidden;
    background: var(--card);
  }
  .card {
    position: relative;
    width: 1200px;
    height: 751px;
    background: var(--card);
    color: var(--ink);
    font-family: "Source Sans 3", "Myriad Pro", Arial, sans-serif;
    font-weight: 400;
  }
  .top-band {
    position: absolute;
    left: 26px;
    right: 22px;
    top: 33px;
    height: 33px;
  }
  .top-band { background: var(--band); }
  .accent-rule {
    position: absolute;
    left: 26px;
    top: 68px;
    width: 940px;
    height: 9px;
    background: linear-gradient(to right, var(--accent) 0%, rgba(46,139,58,0.55) 55%, rgba(46,139,58,0) 100%);
  }
  .brand-name {
    position: absolute;
    left: 84px;
    top: 158px;
    font-size: 68px;
    line-height: 1;
    color: var(--ink);
    white-space: nowrap;
  }
  .person {
    position: absolute;
    left: 88px;
    top: 396px;
  }
  .person-name {
    font-size: 40px;
    line-height: 1.1;
  }
  .person-org {
    font-size: 29px;
    line-height: 1.25;
  }
  .contact {
    position: absolute;
    left: 88px;
    top: 598px;
    font-size: 24px;
    line-height: 1.5;
  }
  .contact .sep { padding: 0 6px; }
</style>
</head>
<body>
  <div class="card">
    <div class="top-band"></div>
    <div class="accent-rule"></div>

    <p class="brand-name">Harvest of Kingdoms</p>

    <div class="person">
      <p class="person-name">Tom Farrel</p>
      <p class="person-org">Harvest of Kingdoms</p>
    </div>

    <div class="contact">
      <p>412 Co. Rd. 118<span class="sep">|</span>Marlow, PA 17602</p>
      <p>Toll free: 570.555.0162<span class="sep">|</span>tomjane4Faith@postvale.com<span class="sep">|</span>www.tf-harvestofkingdoms.com</p>
    </div>
  </div>
</body>
</html>
```